"Hope and Harbour by Mae" Web Site

I would like a web site designed for my funeral and wedding celebrancy business. My logo was designed by Pixel Quarry (attached). I have written content of the web pages for reference (attached). I have attached logos designed through pixel quarry and photos.
I am sure what else to write in a project description and would welcome suggestions

Target Market(s)

for marriages - brides and grooms, for funerals - families who have lost a loved one

Industry/Entity Type

Wedding Planner

Number of Pages Required

4 page

Font styles to use
Sans Serif

Colors
886aae
3277b5
33a6d7
a64599
e34096

Requirements
Must have
• a call to action (contact me) throughout
Nice to have
• nil
Should not have
• no morbid images

```html
<!DOCTYPE html>
<html lang="en">
<head>
<meta charset="utf-8">
<title>Hope and Harbour by Mae</title>
<link rel="stylesheet" href="https://fonts.googleapis.com/css2?family=Poppins:ital,wght@0,400;0,500;0,600;1,400;1,600&family=Oswald:wght@500;600&display=swap">
<style>
:root{
  --purple:#3b2a86;
  --purple-deep:#2e1f6e;
  --lavender:#886aae;
  --lavender-soft:#a994cf;
  --pink:#e0268e;
  --ink:#222222;
  --body:#444444;
  --muted:#777777;
  --line:#d9d9d9;
  --paper:#ffffff;
  --footer:#ececec;
  --dark:#1c1a1f;
}
*{box-sizing:border-box;margin:0;padding:0}
html,body{width:1200px;height:2804px;overflow:hidden}
body{font-family:"Poppins",sans-serif;color:var(--body);background:var(--paper);position:relative}
.abs{position:absolute}

/* header */
.site-header{position:absolute;left:0;top:0;width:1200px;height:137px;background:var(--paper)}
.brand{position:absolute;left:98px;top:60px;display:flex;align-items:center;gap:12px}
.brand-dot{width:30px;height:30px;border-radius:50%;background:var(--lavender);flex:none}
.brand-name{font-family:"Poppins",sans-serif;font-weight:500;font-size:21px;color:var(--purple);line-height:1.15;width:190px}
.call{position:absolute;left:640px;top:30px;display:flex;align-items:center;gap:14px;font-size:21px;color:var(--ink)}
.btn{display:inline-block;background:var(--pink);color:#fff;font-weight:600;text-transform:uppercase;text-align:center;border-radius:3px}
.btn-contact{position:absolute;left:970px;top:25px;width:131px;height:40px;line-height:40px;font-size:15px;background:var(--purple)}
.main-nav{position:absolute;right:98px;top:86px;display:flex;gap:32px;font-size:17px;font-weight:500;color:var(--ink);text-transform:uppercase;letter-spacing:.3px}

/* hero */
.hero{position:absolute;left:0;top:137px;width:1200px;height:620px;overflow:hidden}
.hero-photo{position:absolute;inset:0;background:
  radial-gradient(ellipse 300px 340px at 330px 300px,#b08f6f 0%,rgba(176,143,111,0) 100%),
  linear-gradient(100deg,#5e4d40 0%,#9a836c 25%,#cfc6bd 50%,#ece9e6 70%,#f2f0ee 100%)}
.hero-wave{position:absolute;left:0;bottom:0;width:1200px;height:130px}
.hero-arrow{position:absolute;top:203px;width:36px;height:36px;border-radius:50%;background:#333;display:flex;align-items:center;justify-content:center}
.hero-title{position:absolute;left:760px;top:162px;width:340px;text-align:center}
.hero-title h1{font-family:"Oswald",sans-serif;font-weight:600;font-size:36px;line-height:1.25;color:var(--purple);text-transform:uppercase}

.quote-card{position:absolute;left:780px;top:413px;width:321px;height:402px;background:#fff;box-shadow:0 2px 12px rgba(0,0,0,.25);border-radius:3px;padding:36px 28px 0;text-align:center}
.quote-card h2{font-size:25px;font-weight:500;color:var(--ink);text-transform:uppercase;letter-spacing:.5px}
.quote-card .phone{font-size:19px;color:var(--ink);margin:2px 0 18px}
.field{height:38px;border:1px solid var(--line);border-radius:2px;margin:0 0 13px;text-align:left;font-size:11px;color:var(--muted);padding:0 14px;line-height:38px;position:relative}
.field svg{position:absolute;right:12px;top:15px}
.btn-book{display:block;height:38px;line-height:38px;font-size:15px;margin-top:10px}

/* welcome */
.welcome-photos{position:absolute;left:95px;top:845px;width:430px;height:375px}
.photo-back{position:absolute;left:10px;top:30px;width:360px;height:300px;background:#fff;box-shadow:0 2px 8px rgba(0,0,0,.3);transform:rotate(-6deg)}
.photo-front{position:absolute;left:52px;top:20px;width:370px;height:330px;background:#fff;box-shadow:0 2px 8px rgba(0,0,0,.3);padding:14px}
.photo-front .fill{width:100%;height:100%;background:linear-gradient(135deg,#5d7a3e,#a7b98a 55%,#e8e4df)}
.welcome{position:absolute;left:573px;top:865px;width:552px}
.welcome h2{font-size:29px;font-weight:500;color:var(--ink);line-height:1.4;text-transform:uppercase;margin-bottom:22px}
.welcome p{font-size:12.8px;line-height:1.85;color:var(--body);margin-bottom:14px}
.btn-more{width:111px;height:35px;line-height:35px;font-size:13px;margin-top:16px}

/* services */
.services{position:absolute;left:0;top:1288px;width:1200px;height:662px;background:linear-gradient(160deg,#3a2b80,#2f2170 50%,#3d2d86)}
.section-title{position:absolute;left:0;width:1200px;text-align:center;color:#fff;font-size:35px;font-weight:600}
.divider{position:absolute;left:530px;width:140px;height:20px}
.service{position:absolute;top:190px;width:320px;text-align:center;color:#fff}
.service .wreath{width:250px;height:230px;margin:0 auto;position:relative}
.service .ring{position:absolute;left:0;top:0;width:250px;height:230px;border-radius:50%;border:10px solid var(--lavender-soft);opacity:.55}
.service .pic{position:absolute;left:25px;top:15px;width:200px;height:200px;border-radius:50%;border:4px solid #fff}
.service h3{font-size:28px;font-weight:500;margin:18px 0 10px}
.service p{font-size:12.8px;line-height:1.85;color:#e6e1f2}
.service .more{margin-top:10px}

/* testimonial */
.testimonial{position:absolute;left:0;top:1950px;width:1200px;height:470px;background:linear-gradient(90deg,#141214,#262226 55%,#4a4346)}
.bubble{position:absolute;left:500px;top:48px;width:230px;height:160px}
.quote-text{position:absolute;left:165px;top:220px;width:870px;text-align:center;color:#eee;font-size:13.2px;line-height:1.95}
.quote-name{position:absolute;left:0;top:318px;width:1200px;text-align:center;color:#fff;font-size:16px;font-style:italic}
.quote-name b{font-weight:600}
.dots{position:absolute;left:547px;top:367px;display:flex;gap:6px}
.dots span{width:32px;height:4px;background:#666}
.dots span:first-child{background:#fff}
.testimonial-wave{position:absolute;left:0;top:2330px;width:1200px;height:110px}

/* footer */
.site-footer{position:absolute;left:0;top:2420px;width:1200px;height:315px;background:var(--footer)}
.footer-brand{position:absolute;left:98px;top:120px;display:flex;align-items:center;gap:12px}
.socials{position:absolute;left:145px;top:218px;display:flex;gap:6px}
.socials span{width:23px;height:23px;border-radius:50%;border:1.5px solid #333}
.footer-col{position:absolute;top:72px}
.footer-col h4{font-size:21px;font-weight:500;color:var(--ink);text-transform:uppercase;margin-bottom:22px;letter-spacing:.3px}
.contact-list li{list-style:none;display:flex;gap:14px;font-size:14px;line-height:1.5;color:#333;margin-bottom:14px}
.contact-list svg{flex:none;margin-top:3px}
.links li{list-style:none;font-size:13px;color:#333;line-height:24px;padding-left:20px;position:relative}
.links li:before{content:"";position:absolute;left:4px;top:9px;border-left:5px solid #333;border-top:3.5px solid transparent;border-bottom:3.5px solid transparent}
.news p{font-size:12px;line-height:1.6;color:#555;margin-bottom:14px;width:300px}
.news .input{width:297px;height:40px;border:1px solid var(--line);background:#fff;font-size:12px;color:#555;padding:0 14px;line-height:40px}
.btn-signup{width:121px;height:36px;line-height:36px;font-size:15px;margin-top:16px}
.copyright{position:absolute;left:0;top:2735px;width:1200px;height:69px;background:#fff;border-top:1px solid #ddd;text-align:center;line-height:69px;font-size:12.5px;color:#333}
</style>
</head>
<body>

<header class="site-header">
  <div class="brand">
    <span class="brand-dot"></span>
    <span class="brand-name">Hope and Harbour<br>by Mae</span>
  </div>
  <div class="call">
    <svg width="20" height="20" viewBox="0 0 24 24"><path fill="#222" d="M6.6 10.8a15.1 15.1 0 0 0 6.6 6.6l2.2-2.2a1 1 0 0 1 1-.25 11.4 11.4 0 0 0 3.6.57 1 1 0 0 1 1 1V20a1 1 0 0 1-1 1A17 17 0 0 1 3 4a1 1 0 0 1 1-1h3.5a1 1 0 0 1 1 1c0 1.25.2 2.45.57 3.57a1 1 0 0 1-.25 1z"/></svg>
    <span>Call us : (+61) 0491 570 116</span>
  </div>
  <a class="btn btn-contact">Contact Me</a>
  <nav class="main-nav">
    <span>Home</span><span>About Me</span><span>My Services</span><span>Price</span><span>Blog</span><span>Contact</span>
  </nav>
</header>

<section class="hero">
  <div class="hero-photo" role="img" aria-label="Photo of the celebrant speaking into a microphone at a ceremony"></div>
  <svg class="hero-wave" viewBox="0 0 1200 130" preserveAspectRatio="none">
    <path d="M0 40 C250 150 550 110 800 70 C950 45 1080 30 1200 45 L1200 130 L0 130Z" fill="#fff"/>
    <path d="M0 40 C250 150 550 110 800 70 C950 45 1080 30 1200 45 L1200 55 C1080 45 950 65 800 85 C550 125 250 150 0 60Z" fill="#3b2a86"/>
    <path d="M0 60 C250 150 550 125 800 85 C950 65 1080 45 1200 55 L1200 65 C1080 58 950 78 800 95 C550 130 250 155 0 72Z" fill="#a994cf"/>
  </svg>
  <div class="hero-arrow" style="left:64px"><svg width="14" height="14" viewBox="0 0 14 14"><path d="M9 2 4 7l5 5" stroke="#fff" stroke-width="2.2" fill="none"/></svg></div>
  <div class="hero-arrow" style="left:1130px"><svg width="14" height="14" viewBox="0 0 14 14"><path d="M5 2l5 5-5 5" stroke="#fff" stroke-width="2.2" fill="none"/></svg></div>
  <div class="hero-title">
    <h1>Funeral and Wedding<br>Celebration</h1>
  </div>
</section>

<form class="quote-card">
  <h2>Online Free Quote</h2>
  <p class="phone">(+61) 0491 570 116</p>
  <div class="field">First Name</div>
  <div class="field">Phone</div>
  <div class="field">Services<svg width="10" height="7" viewBox="0 0 10 7"><path d="M1 1l4 4 4-4" stroke="#777" stroke-width="1.4" fill="none"/></svg></div>
  <div class="field">Message</div>
  <a class="btn btn-book">Book an Appointment</a>
</form>

<section>
  <div class="welcome-photos">
    <div class="photo-back"></div>
    <div class="photo-front"><div class="fill" role="img" aria-label="Photo of the celebrant with a bride in a garden"></div></div>
  </div>
  <div class="welcome">
    <h2>Welcome to<br>Hope and Harbour by Mae</h2>
    <p>Thank you for visiting 'Hope and Harbour by Mae'. Whether you are planning a wedding with the love of your life, a funeral to celebrate the life of a loved one or one of many other love and life celebrations, I am glad that you came to 'Hope and Harbour by Mae'.</p>
    <p>My name is Mae Halloran and I am the owner of this business. My mission is to work with you to create a marriage, funeral or celebration service that truly celebrates love and life in an authentic way. Your way!</p>
    <a class="btn btn-more">Read More</a>
  </div>
</section>

<section class="services">
  <h2 class="section-title" style="top:58px">My SERVICES</h2>
  <svg class="divider" style="top:120px" viewBox="0 0 140 20"><line x1="0" y1="10" x2="55" y2="10" stroke="#fff" stroke-width="1.5"/><line x1="85" y1="10" x2="140" y2="10" stroke="#fff" stroke-width="1.5"/><circle cx="70" cy="10" r="9" fill="none" stroke="#fff" stroke-width="1.5"/></svg>

  <div class="service" style="left:90px">
    <div class="wreath"><div class="ring"></div><div class="pic" role="img" aria-label="Photo of a bride and groom" style="background:linear-gradient(135deg,#3a2a22,#8a6d58 50%,#e8ddd2)"></div></div>
    <h3>Marriages</h3>
    <p>Your wedding day is one of the most significant and happy days of your life. Accordingly, you need to choose people and suppliers who can deliver on your wishes and desires</p>
    <svg class="more" width="20" height="14" viewBox="0 0 20 14"><path d="M3 3l7 7 7-7" stroke="#fff" stroke-width="3" fill="none"/></svg>
  </div>
  <div class="service" style="left:440px">
    <div class="wreath"><div class="ring"></div><div class="pic" role="img" aria-label="Photo of white flowers on a memorial table" style="background:linear-gradient(135deg,#2c3a2a,#7b8a70 50%,#e6e6e0)"></div></div>
    <h3>Funerals</h3>
    <p>As the owner of 'Hope and Harbour by Mae', I know that losing a loved one can be a difficult period. We all grieve differently. I feel very privileged to be able to spend</p>
    <svg class="more" width="20" height="14" viewBox="0 0 20 14"><path d="M3 3l7 7 7-7" stroke="#fff" stroke-width="3" fill="none"/></svg>
  </div>
  <div class="service" style="left:788px">
    <div class="wreath"><div class="ring"></div><div class="pic" role="img" aria-label="Photo of a couple walking down the aisle after a ceremony" style="background:linear-gradient(135deg,#6b4b3a,#b58f74 50%,#f0e6dc)"></div></div>
    <h3>Other Ceremonies</h3>
    <p>As a Professional Celebrant, I am also happy to work with you on a range of special events and ceremonies, including: renewal of vows / re-affirmation ceremonies</p>
    <svg class="more" width="20" height="14" viewBox="0 0 20 14"><path d="M3 3l7 7 7-7" stroke="#fff" stroke-width="3" fill="none"/></svg>
  </div>
</section>

<section class="testimonial">
  <svg class="bubble" viewBox="0 0 230 160">
    <path d="M150 15 C215 15 230 80 195 115 L215 150 L160 128 C135 135 110 120 110 120Z" fill="#a994cf"/>
    <circle cx="95" cy="70" r="66" fill="#fff"/>
    <path d="M40 110 L20 150 L80 128Z" fill="#fff"/>
    <circle cx="95" cy="70" r="58" fill="#c9a48c" role="img" aria-label="Portrait photo of a smiling bride"/>
  </svg>
  <p class="quote-text">Sed ut perspiciatis unde omnis iste natus error sit voluptatem accusantium doloremque laudantium, totam rem aperiam, eaque ipsa quae ab illo inventore veritatis et quasi architecto beatae vitae dicta sunt explicabo. Nemo enim ipsam voluptatem quia voluptas sit aspernatur aut odit aut fugit, sed quia consequuntur magni dolores eos qui ratione voluptatem sequi nesciunt.</p>
  <p class="quote-name"><b>Tessa M.</b> - Hope and Harbour by Mae</p>
  <div class="dots"><span></span><span></span><span></span></div>
</section>

<svg class="testimonial-wave abs" viewBox="0 0 1200 110" preserveAspectRatio="none">
  <path d="M0 25 C300 10 700 110 1200 40 L1200 110 L0 110Z" fill="#ececec"/>
  <path d="M0 15 C300 0 700 100 1200 28 L1200 40 C700 110 300 10 0 25Z" fill="#1c1a1f"/>
  <path d="M0 5 C300 -10 700 90 1200 18 L1200 28 C700 100 300 0 0 15Z" fill="#3b2a86"/>
  <path d="M0 -2 C300 -18 700 82 1200 10 L1200 18 C700 90 300 -10 0 5Z" fill="#a994cf"/>
</svg>

<footer class="site-footer">
  <div class="footer-brand">
    <span class="brand-dot"></span>
    <span class="brand-name">Hope and Harbour<br>by Mae</span>
  </div>
  <div class="socials"><span></span><span></span><span></span><span></span></div>

  <div class="footer-col" style="left:355px">
    <h4>Contact Us</h4>
    <ul class="contact-list">
      <li><svg width="14" height="16" viewBox="0 0 14 18"><path d="M7 1a6 6 0 0 0-6 6c0 4.5 6 10 6 10s6-5.5 6-10a6 6 0 0 0-6-6zm0 8.2A2.2 2.2 0 1 1 7 4.8a2.2 2.2 0 0 1 0 4.4z" fill="#333"/></svg><span>Mae Halloran<br>P.O Box 218, Linden<br>6100, Western Australia</span></li>
      <li><svg width="14" height="14" viewBox="0 0 24 24"><path fill="#333" d="M6.6 10.8a15.1 15.1 0 0 0 6.6 6.6l2.2-2.2a1 1 0 0 1 1-.25 11.4 11.4 0 0 0 3.6.57 1 1 0 0 1 1 1V20a1 1 0 0 1-1 1A17 17 0 0 1 3 4a1 1 0 0 1 1-1h3.5a1 1 0 0 1 1 1c0 1.25.2 2.45.57 3.57a1 1 0 0 1-.25 1z"/></svg><span>Phone: (+61) 0491 570 116</span></li>
      <li><svg width="14" height="12" viewBox="0 0 16 12"><path d="M0 0h16v12H0z" fill="#333"/><path d="M1 1l7 5 7-5" stroke="#ececec" stroke-width="1.4" fill="none"/></svg><span>Email: mae@harbourmail.net.au</span></li>
    </ul>
  </div>

  <div class="footer-col" style="left:620px">
    <h4>Quick Links</h4>
    <ul class="links"><li>Home</li><li>About me</li><li>My Services</li><li>Price</li><li>Blog</li><li>Contact</li></ul>
  </div>

  <div class="footer-col news" style="left:803px">
    <h4>Sign Up for Newsletter</h4>
    <p>Excepteur sint occaecat cupidatat non proident, sunt in culpa qui officia deserunt</p>
    <div class="input">Enter email</div>
    <a class="btn btn-signup">Sign Up</a>
  </div>
</footer>

<div class="copyright">© Copyright 2018 Hope and Harbour by Mae. All Rights Reserved.</div>

</body>
</html>
```